Automotive Brand Survey Online

Hi guys, we are looking for a freelancer who can design User Interface design (UI) for a survey-online website layout. <br/><br/>For the content, there are question, choices, back and next buttons - as if you are designing a survey website.<br/><br/>There are 5 main contents of the website consists of:<br/>1. Single-answer question<br/>2. Yes/No-answer question<br/>3. Net Promoter Score (NPS) or 1-5 scale question<br/>4. Open-end question<br/>5. Thank you page when finish survey<br/><br/>Here is the demo and more description<br/>https://demo.quorvel.link/survey/
Target Market(s)
Car Owner
Industry/Entity Type
Automotive
Number of Pages Required
1 page

```html
<!DOCTYPE html>
<html lang="en">
<head>
<meta charset="utf-8">
<title>Quorvel Survey – Open-end Question</title>
<link href="https://fonts.googleapis.com/css2?family=Noto+Sans:wght@400;600;700&display=swap" rel="stylesheet">
<style>
  :root {
    --page-bg: #282828;
    --header-bg: #ebebeb;
    --brand-box: #282828;
    --accent: #6cc5a3;
    --ink-dark: #333333;
    --ink-muted: #9a9a9a;
    --track-line: #a8a8a8;
    --field-bg: #ffffff;
    --placeholder: #8a8a8a;
    --back-btn: #253f5b;
    --next-btn: #c8163f;
    --white: #ffffff;
  }
  * { box-sizing: border-box; margin: 0; padding: 0; }
  html, body {
    width: 675px;
    height: 1200px;
    overflow: hidden;
  }
  body {
    position: relative;
    background: var(--page-bg);
    font-family: "Noto Sans", Arial, sans-serif;
  }
  .site-header {
    position: absolute;
    left: 0; top: 0;
    width: 675px; height: 150px;
    background: var(--header-bg);
    box-shadow: 0 4px 14px rgba(0,0,0,0.35);
  }
  .brand {
    position: absolute;
    left: 37.5px; top: 37.5px;
    width: 75px; height: 75px;
    background: var(--brand-box);
    display: flex;
    align-items: center;
    justify-content: center;
  }
  .brand-name {
    color: var(--accent);
    font-size: 12px;
    font-weight: 600;
    letter-spacing: 0.5px;
  }
  .progress-title {
    position: absolute;
    left: 334px; top: 40px;
    font-size: 15px;
    font-weight: 600;
    color: var(--ink-dark);
    white-space: nowrap;
  }
  .progress-title .value { margin-left: 8px; }
  .progress-labels {
    position: absolute;
    left: 0; top: 75px;
    width: 675px; height: 16px;
  }
  .progress-labels span {
    position: absolute;
    transform: translateX(-50%);
    font-size: 11.5px;
    font-weight: 600;
    color: var(--ink-muted);
  }
  .progress-labels .current { color: var(--accent); }
  .progress-track {
    position: absolute;
    left: 337px; top: 100px;
  }
  .survey-question {
    position: absolute;
    left: 37.5px; top: 215px;
    font-size: 30px;
    font-weight: 600;
    color: var(--white);
    white-space: nowrap;
    letter-spacing: -0.1px;
  }
  .survey-question .q-number { color: var(--accent); }
  .comment-field {
    position: absolute;
    left: 37.5px; top: 297.5px;
    width: 600px; height: 186px;
    background: var(--field-bg);
    border: 1px solid var(--accent);
    border-radius: 4px;
    padding: 16px 24px;
    font-family: inherit;
    font-size: 22px;
    font-weight: 600;
    color: var(--ink-dark);
    resize: none;
    outline: none;
  }
  .comment-field::placeholder { color: var(--placeholder); }
  .nav-button {
    position: absolute;
    top: 609.5px;
    width: 219px; height: 50px;
    border: none;
    border-radius: 4px;
    font-family: inherit;
    font-size: 20px;
    font-weight: 700;
    color: var(--white);
    display: flex;
    align-items: center;
    justify-content: center;
  }
  .nav-button.back { left: 74px; background: var(--back-btn); }
  .nav-button.next { left: 383px; background: var(--next-btn); }
  .nav-button .chevron {
    position: absolute;
    right: 18px; top: 16px;
  }
</style>
</head>
<body>
  <header class="site-header">
    <div class="brand"><span class="brand-name">QUORVEL</span></div>
    <div class="progress-title">Your Progress:<span class="value">0% Complete</span></div>
    <div class="progress-labels">
      <span class="current" style="left:344px">0%</span>
      <span style="left:415px">25%</span>
      <span style="left:487px">50%</span>
      <span style="left:559px">75%</span>
      <span style="left:631px">100%</span>
    </div>
    <svg class="progress-track" width="301" height="13" viewBox="0 0 301 13" aria-hidden="true">
      <rect x="0.75" y="0.75" width="299.5" height="11.5" rx="3" fill="#ffffff" stroke="var(--track-line)" stroke-width="1.5"/>
      <circle cx="6.5" cy="6.5" r="3" fill="var(--accent)"/>
      <circle cx="78" cy="6.5" r="3" fill="var(--track-line)"/>
      <circle cx="150" cy="6.5" r="3" fill="var(--track-line)"/>
      <circle cx="222" cy="6.5" r="3" fill="var(--track-line)"/>
      <circle cx="294" cy="6.5" r="3" fill="var(--track-line)"/>
    </svg>
  </header>

  <main>
    <h1 class="survey-question"><span class="q-number">S1.</span> How do you feel with this car model?</h1>
    <textarea class="comment-field" placeholder="Enter your comments here" aria-label="Your comments"></textarea>
    <button class="nav-button back" type="button">BACK</button>
    <button class="nav-button next" type="button">NEXT
      <svg class="chevron" width="12" height="18" viewBox="0 0 12 18" aria-hidden="true">
        <polyline points="2,2 9,9 2,16" fill="none" stroke="#ffffff" stroke-width="2.5" stroke-linecap="round" stroke-linejoin="round"/>
      </svg>
    </button>
  </main>
</body>
</html>
```